Gym Poster to advertise for our chiropractic business

We are needing a poster for a gym. They are a weight training gym, Copper Ridge Gym. The poster will be 4 ft by 8 ft. This poster will be used for advertising purposes.
Target Market(s)
Athletes, 25 to 45,Men and Women,
Industry/Entity Type
Advertising
Font styles to use
Serif
Sans Serif

```html
<!DOCTYPE html>
<html lang="en">
<head>
<meta charset="utf-8">
<title>Ridgeline Chiropractic – Poster</title>
<link rel="stylesheet" href="https://fonts.googleapis.com/css2?family=Arimo:wght@400;600;700&display=swap">
<style>
  :root {
    --navy: #1d2f4c;
    --panel-blue: #87aed1;
    --white: #ffffff;
    --skin-light: #e6c6ad;
    --skin-mid: #c99a7c;
    --sheet: #efece8;
  }
  * { margin: 0; padding: 0; box-sizing: border-box; }
  html, body { width: 1200px; height: 562px; overflow: hidden; background: var(--white); }
  .poster {
    position: relative;
    width: 1200px;
    height: 562px;
    font-family: "Arimo", Arial, sans-serif;
    overflow: hidden;
  }
  .brand {
    position: absolute;
    left: 0; top: 0;
    width: 510px; height: 215px;
    background: var(--white);
    display: flex;
    align-items: center;
    justify-content: center;
  }
  .brand-name {
    color: var(--navy);
    font-size: 30px;
    font-weight: 600;
    letter-spacing: 0.3px;
    white-space: nowrap;
  }
  .treatment-photo {
    position: absolute;
    left: 0; top: 215px;
    width: 510px; height: 347px;
    background:
      radial-gradient(ellipse at 70% 60%, var(--skin-light) 0%, var(--skin-mid) 55%, transparent 80%),
      linear-gradient(160deg, var(--sheet) 0%, var(--skin-mid) 50%, var(--sheet) 100%);
  }
  .info-panel {
    position: absolute;
    left: 510px; top: 0;
    width: 690px; height: 562px;
    background: var(--panel-blue);
    color: var(--white);
  }
  .headline {
    position: absolute;
    top: 24px; left: 0; right: 0;
    text-align: center;
    font-size: 25.5px;
    font-weight: 400;
    line-height: 31px;
    letter-spacing: 1px;
    word-spacing: 3px;
  }
  .headline strong { font-weight: 700; }
  .services { list-style: none; }
  .services li {
    position: absolute;
    font-size: 18px;
    font-weight: 700;
    letter-spacing: 0.7px;
    transform: translateY(-50%);
    white-space: nowrap;
  }
  .cta {
    position: absolute;
    top: 479px; left: 0; right: 0;
    text-align: center;
    font-size: 26px;
    letter-spacing: 1px;
  }
  .contact {
    position: absolute;
    top: 514px; left: 0; right: 0;
    text-align: center;
    font-size: 14.5px;
    line-height: 20px;
    letter-spacing: 0.8px;
  }
</style>
</head>
<body>
<div class="poster">
  <header class="brand">
    <p class="brand-name">Ridgeline Chiropractic LLC</p>
  </header>

  <div class="treatment-photo" role="img" aria-label="Photo of a chiropractor's hands pressing on a patient's lower back"></div>

  <section class="info-panel">
    <h1 class="headline">When <strong>YOU</strong> are suffering we offer the best<br>treatments and care available.</h1>

    <ul class="services">
      <li style="left:265px; top:155px;">Chiropractic Adjustments</li>
      <li style="left:261px; top:189px;">Spinal Curve Correction</li>
      <li style="left:307px; top:222px;">Myofacial Release</li>
      <li style="left:302px; top:255px;">Massage Therapy</li>
      <li style="left:319px; top:287px;">Rehabilitation Services</li>
      <li style="left:335px; top:320px;">Strapping</li>
      <li style="left:345px; top:352px;">Sports Taping</li>
      <li style="left:337px; top:384px;">Orthotics and Bracing</li>
      <li style="left:324px; top:415px;">Supplementation</li>
    </ul>

    <p class="cta">We offer same day appointments!</p>
    <p class="contact">www.ridgelinespine.com<br>2280 Elm Park Avenue, Dallas, TX 75230 &nbsp;|&nbsp; Tel: 469.555.0187</p>
  </section>
</div>
</body>
</html>
```